Invitation Design Project

50th Birthday Party for Tim. Big, loud party planned with loads of friends and family. at our home. Decorations will be coloured lanterns attached to the pergola and hired a band.

Details:

on 19th October, 2013
(other details when design chosen)
at: 7.00 pm
RSVP: 14th October, 2013

```html
<!DOCTYPE html>
<html lang="en">
<head>
<meta charset="utf-8">
<title>Tim's 50th Birthday Party Invitation</title>
<link href="https://fonts.googleapis.com/css2?family=Pacifico&family=Open+Sans:wght@300;400&display=swap" rel="stylesheet">
<style>
  :root {
    --ink: #111111;
    --paper: #ffffff;
    --outline: #0b0b0b;
    --hot-red: #e8242a;
    --orange: #f27a1a;
    --magenta: #b0357f;
    --violet: #5a3fb0;
    --royal-blue: #2a4fc4;
    --deep-navy: #151a4a;
    --green: #2f9a4a;
  }
  * { margin: 0; padding: 0; box-sizing: border-box; }
  html, body {
    width: 848px;
    height: 1200px;
    overflow: hidden;
    background: var(--paper);
  }
  .invitation {
    position: relative;
    width: 848px;
    height: 1200px;
    overflow: hidden;
    font-family: "Open Sans", Arial, sans-serif;
    color: var(--ink);
  }
  .party-scene {
    position: absolute;
    inset: 0;
    background:
      radial-gradient(ellipse 420px 520px at 90px 900px, var(--green) 0%, transparent 70%),
      radial-gradient(ellipse 520px 600px at 60px 150px, var(--hot-red) 0%, transparent 75%),
      radial-gradient(ellipse 380px 420px at 330px 380px, var(--orange) 0%, transparent 70%),
      radial-gradient(ellipse 520px 700px at 560px 250px, var(--magenta) 0%, transparent 75%),
      radial-gradient(ellipse 600px 800px at 800px 500px, var(--royal-blue) 0%, transparent 80%),
      linear-gradient(160deg, var(--violet) 0%, var(--deep-navy) 100%);
  }
  .title {
    position: absolute;
    left: 0;
    width: 848px;
    text-align: center;
    font-family: "Pacifico", cursive;
    color: var(--paper);
    line-height: 1;
    -webkit-text-stroke: 6px var(--outline);
    paint-order: stroke fill;
  }
  .title--name { top: 300px; font-size: 42px; }
  .title--occasion { top: 378px; font-size: 64px; }
  .title--party { top: 478px; font-size: 48px; }
  .details-card {
    position: absolute;
    left: 96px;
    top: 603px;
    width: 656px;
    height: 549px;
    background: var(--paper);
    text-align: center;
  }
  .verse-shout {
    position: absolute;
    top: 42px;
    width: 100%;
    font-weight: 300;
    font-size: 26px;
    line-height: 36px;
    text-transform: uppercase;
  }
  .verse-cheer {
    position: absolute;
    top: 154px;
    width: 100%;
    font-weight: 400;
    font-size: 25px;
    line-height: 36px;
  }
  .event-name {
    position: absolute;
    top: 282px;
    width: 100%;
    font-family: "Pacifico", cursive;
    font-size: 36px;
    line-height: 1.2;
  }
  .event-date {
    position: absolute;
    top: 347px;
    width: 100%;
    font-weight: 300;
    font-size: 19px;
  }
  .event-venue {
    position: absolute;
    top: 448px;
    width: 100%;
    font-weight: 400;
    font-size: 21px;
    line-height: 32px;
  }
</style>
</head>
<body>
  <main class="invitation">
    <div class="party-scene" role="img" aria-label="Photograph of people dancing in silhouette at a party under colourful red, orange, purple and blue disco lights"></div>

    <h1>
      <span class="title title--name">Tim's</span>
      <span class="title title--occasion">50th Birthday</span>
      <span class="title title--party">Party</span>
    </h1>

    <section class="details-card">
      <p class="verse-shout">The big 5-0 is approaching fast<br>Tim is over the hill at last!</p>
      <p class="verse-cheer">Come celebrate and spread some cheer<br>And let Dean know he's old this year!</p>
      <h2 class="event-name">Tim's 50th Birthday Party</h2>
      <p class="event-date">19th October, 2013,&nbsp; 7.00 pm</p>
      <p class="event-venue">Tim’s Home<br>RSVP&nbsp; 14th October, 2013</p>
    </section>
  </main>
</body>
</html>
```